Valduro.com needs a Mobile FIRST Site

Valduro.com is an insurance broker based in Panama City, Panama that plans to sell car and motorcycle insurance online.

We need to design a total of 5 pages (two of those are A/B test pages). The site will be responsive and will be programmed in React. We will be using Brisk Widget´s library to code Valduro.com. Keep in mind that we are using Brisk Widget to program the site´s functions, not to create the "look and feel" of the site, that is obviously your job. You can learn more about Brisk Widget here... https://brisk-widget.example/

We have created wireframes for the app. Please follow and keep in mind the instructions in the wireframes. You can change things here and there as long as the core functions and goals stay intact. We have uploaded the wireframes along with the company logo and color.

We are planning to A/B test the site´s home page so we need to design two homepages. You can find homepage A and B in the wireframes provided.

We speak Spanish in Panama but you can design the site in English. We can change the text once we receive the designs.

Target Market(s)

25-45 year olds who own a car or motorcylcle and own a credit card.

Industry/Entity Type

Insurance

Font styles to use
Sans Serif

Requirements
Must have
• Follow the wireframes provided and the logo colors.
Nice to have
• Please look at the Image I´ve uploaded from DeskHaven, use it as reference to create HomePage A.

```html
<!DOCTYPE html>
<html lang="en">
<head>
<meta charset="utf-8">
<title>Valduro.com — Auto Insurance</title>
<link href="https://fonts.googleapis.com/css2?family=Mulish:wght@400;600;700;800&display=swap" rel="stylesheet">
<style>
:root{
  --brand:#3d2b86;
  --brand-dark:#2f1f6e;
  --ink:#222;
  --muted:#666;
  --line:#e4e4e4;
  --accent:#e8544f;
  --footer:#f0f0f2;
  --white:#fff;
}
*{box-sizing:border-box;margin:0;padding:0}
html,body{width:853px;height:1200px;overflow:hidden}
body{font-family:'Mulish',sans-serif;color:var(--ink);background:var(--white);position:relative}
.abs{position:absolute}

/* header */
.site-header{position:absolute;left:0;top:0;width:853px;height:66px;background:var(--brand)}
.brand{position:absolute;left:62px;top:16px;color:var(--white);font-weight:800;font-size:29px;letter-spacing:-.5px;line-height:1}
.brand small{font-size:8px;font-weight:800;margin-left:2px}
.nav a{position:absolute;top:27px;color:var(--white);font-size:10.5px;text-decoration:none;font-weight:600}
.search{position:absolute;left:561px;top:20px;width:167px;height:26px;background:var(--white);border-radius:2px;border:2px solid #ddd}
.search span{position:absolute;left:8px;top:5px;font-size:9px;color:#999}
.search .btn{position:absolute;right:2px;top:2px;width:18px;height:18px;background:var(--brand);border-radius:2px}
.cart{position:absolute;left:754px;top:20px}

/* hero */
.hero{position:absolute;left:0;top:66px;width:853px;height:328px;
  background:linear-gradient(100deg,#7d8478 0%,#9ea3a3 30%,#6f7479 55%,#3b3c40 75%,#2a2a2e 100%)}
.hero-title{position:absolute;left:62px;top:128px;color:var(--white);font-size:24px;line-height:29px;font-weight:400}
.hero-title b{font-weight:800}
.hero-btn{position:absolute;left:62px;top:234px;width:105px;height:26px;border:1px solid var(--white);color:var(--white);font-size:10px;font-weight:700;text-align:center;line-height:24px;letter-spacing:.3px}
.dot{position:absolute;left:781px;width:9px;height:9px;border:1px solid var(--white);border-radius:50%}
.dot.on{background:var(--white)}

/* steps */
.steps{position:absolute;left:125px;top:328px;width:603px;height:130px;background:var(--white);box-shadow:0 8px 18px rgba(0,0,0,.06)}
.step-line{position:absolute;top:54px;height:0;border-top:1px dashed #cfcfcf}
.step{position:absolute;top:28px;width:52px;height:52px;border-radius:50%;border:2px solid #9a9a9a;text-align:center;line-height:48px;font-size:18px;color:#555}
.step.done{background:var(--brand);border-color:var(--brand)}
.step.wait{border-color:#cfcfcf;color:#bbb}
.step-label{position:absolute;top:90px;width:120px;text-align:center;font-size:12.5px;font-weight:600}

/* products */
.section-title{position:absolute;left:0;width:853px;top:505px;text-align:center;color:var(--brand);font-size:24px;font-weight:600}
.rule{position:absolute;top:520px;height:1px;background:#ccc;width:62px}
.arrow{position:absolute;top:555px;width:26px;height:26px;border-radius:50%;background:var(--white);box-shadow:0 1px 4px rgba(0,0,0,.15)}
.tabs{position:absolute;left:312px;top:555px;width:229px;height:27px;border-radius:14px;background:#ececef}
.tab{position:absolute;top:0;height:27px;font-size:11.5px;line-height:27px}
.tab.active{left:0;width:114px;background:var(--brand);color:var(--white);border-radius:14px 0 0 14px}
.tab.active::after{content:"";position:absolute;left:52px;bottom:-6px;border:5px solid transparent;border-top-color:var(--brand);border-bottom:0}
.tab.idle{left:114px;width:115px;color:var(--ink)}

.card{position:absolute;top:614px;width:168px;height:420px;border:1px solid #e6e6e6;background:var(--white)}
.card.lift{box-shadow:0 4px 16px rgba(0,0,0,.1);border-color:#f0f0f0}
.badge{position:absolute;left:-1px;top:-1px;width:20px;height:19px;background:var(--accent)}
.insurer{position:absolute;left:0;top:18px;width:100%;height:92px;display:flex;align-items:center;justify-content:center;flex-direction:column;gap:6px}
.insurer .mark{width:26px;height:26px;border-radius:50%;background:var(--brand)}
.insurer .name{font-size:13px;font-weight:800;color:var(--ink);text-align:center;line-height:1.15}
.price{position:absolute;left:0;top:122px;width:100%;text-align:center;color:var(--brand);font-size:13px;font-weight:600}
.price::before,.price::after{content:"";display:inline-block;width:22px;border-top:1px dashed #ccc;vertical-align:middle;margin:0 8px}
.card-rule{position:absolute;left:13px;width:141px;height:1px;background:var(--line)}
.spec{position:absolute;left:13px;font-size:11.5px;letter-spacing:.2px}
.spec em{display:block;font-style:normal;color:var(--brand);font-size:10.5px;font-weight:700;margin-top:3px}
.benefits{position:absolute;left:13px;top:296px;font-size:13px}
.benefits ul{list-style:none;margin-top:9px}
.benefits li{font-size:9.5px;color:var(--muted);height:15.5px;letter-spacing:.2px}
.benefits li::before{content:"»";color:var(--brand);margin-right:5px;font-weight:700}
.buy{position:absolute;left:13px;top:376px;width:92px;height:25px;border:1px solid var(--brand);color:var(--brand);font-size:10.5px;text-align:center;line-height:23px}
.buy.solid{background:var(--brand);color:var(--white)}
.compare{position:absolute;left:115px;top:376px;width:25px;height:25px;border:1px solid var(--brand);display:flex;align-items:center;justify-content:center}

.view-all{position:absolute;left:367px;top:1066px;width:118px;height:28px;border:1px solid var(--brand);color:var(--brand);font-size:10.5px;text-align:center;line-height:26px;letter-spacing:.3px}

/* footer */
.site-footer{position:absolute;left:0;top:1148px;width:853px;height:52px;background:var(--footer)}
.foot-brand{position:absolute;left:62px;top:12px;color:var(--brand);font-weight:800;font-size:23px;letter-spacing:-.4px}
.foot-brand small{font-size:7px}
.copy{position:absolute;left:206px;top:20px;font-size:9.5px;color:var(--muted);letter-spacing:.2px}
.copy b{color:var(--brand);font-weight:600}
.legal{position:absolute;top:20px;font-size:9.5px;color:var(--muted);letter-spacing:.2px}
.legal.current{color:var(--brand);text-decoration:underline}
.to-top{position:absolute;left:748px;top:0;width:42px;height:52px;background:var(--brand);display:flex;align-items:center;justify-content:center}
</style>
</head>
<body>

<header class="site-header">
  <div class="brand">Valduro<small>.com</small></div>
  <nav class="nav">
    <a style="left:272px">-- Home --</a>
    <a style="left:347px">About Us</a>
    <a style="left:415px">Products</a>
    <a style="left:481px">Contact Us</a>
  </nav>
  <div class="search"><span>Search...</span>
    <div class="btn"><svg width="18" height="18" viewBox="0 0 18 18"><circle cx="8" cy="8" r="3.5" fill="none" stroke="#fff" stroke-width="1.5"/><line x1="10.5" y1="10.5" x2="13" y2="13" stroke="#fff" stroke-width="1.5"/></svg></div>
  </div>
  <svg class="cart" width="36" height="30" viewBox="0 0 36 30">
    <path d="M2 5h5l4 13h14l3-9H9" fill="none" stroke="#fff" stroke-width="2"/>
    <circle cx="13" cy="23" r="2" fill="#fff"/><circle cx="23" cy="23" r="2" fill="#fff"/>
    <circle cx="29" cy="6" r="5" fill="#fff"/><text x="29" y="9" font-size="7" text-anchor="middle" fill="#3d2b86" font-family="Mulish,sans-serif" font-weight="700">0</text>
  </svg>
</header>

<section class="hero" role="img" aria-label="Photo of a dark hatchback car speeding along a winding road">
</section>
<h1 class="hero-title abs">We Have <b>Excellent Plans</b><br><b>Available</b> Through Reputable<br><b>Auto Insurers!</b></h1>
<div class="hero-btn">Contact Us</div>
<span class="dot" style="top:177px"></span>
<span class="dot on" style="top:193px"></span>
<span class="dot" style="top:208px"></span>

<div class="steps">
  <div class="step-line" style="left:119px;width:137px"></div>
  <div class="step-line" style="left:328px;width:137px"></div>
  <div class="step done" style="left:67px"><svg width="48" height="48" viewBox="0 0 48 48"><path d="M17 24l5 5 9-10" fill="none" stroke="#fff" stroke-width="3"/></svg></div>
  <div class="step" style="left:276px">2</div>
  <div class="step wait" style="left:484px">3</div>
  <div class="step-label" style="left:33px">Finished</div>
  <div class="step-label" style="left:242px">In Progress</div>
  <div class="step-label" style="left:450px">Waiting</div>
</div>

<h2 class="section-title">Our Products</h2>
<span class="rule" style="left:272px"></span>
<span class="rule" style="left:519px"></span>

<div class="arrow" style="left:133px"><svg width="26" height="26" viewBox="0 0 26 26"><path d="M14.5 10l-3 3 3 3" fill="none" stroke="#333" stroke-width="1.2"/></svg></div>
<div class="arrow" style="left:694px"><svg width="26" height="26" viewBox="0 0 26 26"><path d="M11.5 10l3 3-3 3" fill="none" stroke="#333" stroke-width="1.2"/></svg></div>

<div class="tabs">
  <div class="tab active"><svg class="abs" style="left:35px;top:8px" width="14" height="11" viewBox="0 0 14 11"><path d="M2 5l2-4h6l2 4v4H2z" fill="#fff"/><circle cx="4" cy="9" r="1.4" fill="#3d2b86"/><circle cx="10" cy="9" r="1.4" fill="#3d2b86"/></svg><span class="abs" style="left:54px">Cars</span></div>
  <div class="tab idle"><svg class="abs" style="left:16px;top:8px" width="16" height="11" viewBox="0 0 16 11"><circle cx="3.5" cy="7" r="3" fill="none" stroke="#222" stroke-width="1.3"/><circle cx="12.5" cy="7" r="3" fill="none" stroke="#222" stroke-width="1.3"/><path d="M3.5 7l4-4h3l2 4" fill="none" stroke="#222" stroke-width="1.3"/></svg><span class="abs" style="left:39px">Motorcycle</span></div>
</div>

<!-- product cards -->
<article class="card" style="left:62px">
  <span class="badge"><svg width="20" height="19" viewBox="0 0 20 19"><path d="M10 4l1.6 3.4 3.6.4-2.7 2.4.8 3.6L10 12l-3.3 1.8.8-3.6L4.8 7.8l3.6-.4z" fill="#fff"/></svg></span>
  <div class="insurer"><span class="mark"></span><span class="name">Crestline<br>Insurance</span></div>
  <div class="price">$150.00</div>
  <div class="card-rule" style="top:146px"></div>
  <div class="spec" style="top:160px">Insurance Coverage<em>$ 10,000</em></div>
  <div class="spec" style="top:199px">Maximum Amount<em>$ 15,000</em></div>
  <div class="spec" style="top:238px">Insurance Limit<em>$ 20,000</em></div>
  <div class="card-rule" style="top:278px"></div>
  <div class="benefits">Benefits<ul><li>There are many variations</li><li>Lorem Ipsum simply</li><li>Discovered Undoubtable</li></ul></div>
  <div class="buy">Buy Now!</div>
  <div class="compare"><svg width="11" height="9" viewBox="0 0 11 9"><path d="M1 4V2h8M7 0l2 2-2 2M10 5v2H2M4 9L2 7l2-2" fill="none" stroke="#3d2b86" stroke-width="1.3"/></svg></div>
</article>

<article class="card" style="left:250px">
  <div class="insurer"><span class="name">Harbor<br>Mutual</span></div>
  <div class="price">$120.00</div>
  <div class="card-rule" style="top:146px"></div>
  <div class="spec" style="top:160px">Insurance Coverage<em>$ 10,000</em></div>
  <div class="spec" style="top:199px">Maximum Amount<em>$ 15,000</em></div>
  <div class="spec" style="top:238px">Accident Limit<em>$ 10,000</em></div>
  <div class="card-rule" style="top:278px"></div>
  <div class="benefits">Benefits<ul><li>There are many variations</li><li>Lorem Ipsum simply</li></ul></div>
  <div class="buy">Buy Now!</div>
  <div class="compare"><svg width="11" height="9" viewBox="0 0 11 9"><path d="M1 4V2h8M7 0l2 2-2 2M10 5v2H2M4 9L2 7l2-2" fill="none" stroke="#3d2b86" stroke-width="1.3"/></svg></div>
</article>

<article class="card lift" style="left:436px">
  <span class="badge"><svg width="20" height="19" viewBox="0 0 20 19"><path d="M10 4l1.6 3.4 3.6.4-2.7 2.4.8 3.6L10 12l-3.3 1.8.8-3.6L4.8 7.8l3.6-.4z" fill="#fff"/></svg></span>
  <div class="insurer"><span class="name">Northgate<br>Insurance Group</span></div>
  <div class="price">$150.00</div>
  <div class="card-rule" style="top:146px"></div>
  <div class="spec" style="top:160px">Insurance Coverage<em>$ 10,000</em></div>
  <div class="spec" style="top:199px">Maximum Amount<em>$ 15,000</em></div>
  <div class="spec" style="top:238px">Insurance Limit<em>$ 20,000</em></div>
  <div class="card-rule" style="top:278px"></div>
  <div class="benefits">Benefits<ul><li>There are many variations</li><li>Lorem Ipsum simply</li><li>Discovered Undoubtable</li></ul></div>
  <div class="buy solid">Buy Now!</div>
  <div class="compare"><svg width="11" height="9" viewBox="0 0 11 9"><path d="M1 4V2h8M7 0l2 2-2 2M10 5v2H2M4 9L2 7l2-2" fill="none" stroke="#3d2b86" stroke-width="1.3"/></svg></div>
</article>

<article class="card" style="left:623px">
  <div class="insurer"><span class="mark"></span><span class="name">Prairie<br>Auto</span></div>
  <div class="price">$120.00</div>
  <div class="card-rule" style="top:146px"></div>
  <div class="spec" style="top:160px">Insurance Coverage<em>$ 10,000</em></div>
  <div class="spec" style="top:199px">Maximum Amount<em>$ 15,000</em></div>
  <div class="spec" style="top:238px">Accident Limit<em>$ 10,000</em></div>
  <div class="card-rule" style="top:278px"></div>
  <div class="benefits">Benefits<ul><li>There are many variations</li><li>Lorem Ipsum simply</li></ul></div>
  <div class="buy">Buy Now!</div>
  <div class="compare"><svg width="11" height="9" viewBox="0 0 11 9"><path d="M1 4V2h8M7 0l2 2-2 2M10 5v2H2M4 9L2 7l2-2" fill="none" stroke="#3d2b86" stroke-width="1.3"/></svg></div>
</article>

<div class="view-all">View All Products</div>

<footer class="site-footer">
  <div class="foot-brand">Valduro<small>.com</small></div>
  <div class="copy">© 2018 <b>Valduro</b>. All Rights Reserved.</div>
  <span class="legal current" style="left:418px">Disclaimer</span>
  <span class="legal" style="left:481px">|</span>
  <span class="legal" style="left:495px">Terms and Conditions</span>
  <span class="legal" style="left:611px">|</span>
  <span class="legal" style="left:625px">Privacy Policy</span>
  <div class="to-top"><svg width="10" height="10" viewBox="0 0 10 10"><path d="M2 5l3-3 3 3M2 8l3-3 3 3" fill="none" stroke="#fff" stroke-width="1.3"/></svg></div>
</footer>

</body>
</html>
```